Skin care line needs a LABEL designed!

Fennow Skin Care... An EARTHY modern boho chic skin care line needs a label designed. It is called Fennow because there are healing crystals in the product. Holistic, yoga feel, Earthy, feminine.

This contest is for 1 cleanser label- 2 different versions:

Gel Cleanser
Milk Cleanser

Label Size: 4.8125 x 4.8125 in

Winner will be selected to do the labels for:
Toner (5 Versions)
Serum (5 Versions)
Moisturizer (3 Versions)
Sample Label and packaging

Please be prepared to quote a price for the additional labels listed.

Inspiring Brands: **Marsk Studio**, Tarbell Organics, Celia Drummet, Quillhaven beauty product brands,

Feel free to separate the logo symbol and use it somewhere else in the design.

Target Market(s)

Women ages 30-60

Industry/Entity Type

Skin Care Product

Requirements
Must have
• Tag Line: Inner Peace- Outer Beauty
• Area for ingredients
• Earthy feel
• Large STEP 1 on the front of packaging
• Disclaimer:
• Note: Metaphysical descriptions and healing properties of crystals are not meant to replace medical advice or treat any condition. For external use only.
Nice to have
• www.fennow-skincare-example.com
Should not have
• Multiple Colors

```html
<!DOCTYPE html>
<html lang="en">
<head>
<meta charset="utf-8">
<title>Fennow Skin Care — Cleanser Gel Label</title>
<link rel="stylesheet" href="https://fonts.googleapis.com/css2?family=Dancing+Script:wght@500&family=Arimo:wght@400;700&display=swap">
<style>
  :root {
    --backdrop: #f6f6f6;
    --label-light: #ececec;
    --label-mid: #dedede;
    --rule: #c9c9c9;
    --accent-blue: #1a93d6;
    --feather-blue: #a9d4ea;
    --ghost-feather: #e2e2e2;
    --ink-gray: #9a9a9a;
    --mark-gray: #8c8c8c;
  }
  * { margin: 0; padding: 0; box-sizing: border-box; }
  html, body {
    width: 1200px; height: 870px; overflow: hidden;
    background: radial-gradient(ellipse at 50% 45%, #ffffff 0%, var(--backdrop) 70%, #ededed 100%);
    font-family: "Arimo", Arial, sans-serif;
  }
  .label {
    position: absolute; left: 230px; top: 46px;
    width: 748px; height: 752px;
    background: radial-gradient(ellipse at 45% 35%, var(--label-light) 0%, var(--label-mid) 100%);
    overflow: hidden;
  }
  .label__sheen {
    position: absolute; left: 0; top: 0; width: 748px; height: 752px;
  }
  .divider {
    position: absolute; top: 62px; width: 3px; height: 634px;
    background: var(--rule);
  }
  .divider--left { left: 306px; }
  .divider--right { left: 342px; }
  .ghost-feather {
    position: absolute; left: 38px; top: 126px; width: 230px; height: 444px;
    background: radial-gradient(ellipse at 55% 45%, var(--ghost-feather) 0%, rgba(226,226,226,0) 70%);
    border-radius: 50% 50% 45% 45%;
    transform: rotate(-12deg);
  }
  .ingredients {
    position: absolute; left: 12px; top: 664px; width: 290px;
    font-size: 7.4px; line-height: 10.5px; color: var(--ink-gray);
  }
  .feather-art {
    position: absolute; left: 466px; top: 110px; width: 204px; height: 128px;
    background: linear-gradient(200deg, var(--feather-blue) 0%, rgba(169,212,234,0.45) 100%);
    border-radius: 70% 20% 60% 30%;
    transform: rotate(-18deg);
    opacity: 0.85;
  }
  .feather-shadow {
    position: absolute; left: 532px; top: 262px; width: 110px; height: 8px;
    background: radial-gradient(ellipse, rgba(160,160,160,0.35) 0%, rgba(160,160,160,0) 70%);
  }
  .product-name {
    position: absolute; left: 364px; top: 268px; width: 376px;
    font-family: "Dancing Script", cursive;
    font-weight: 500; font-size: 84px; line-height: 96px;
    color: var(--accent-blue); text-align: center;
  }
  .product-type {
    position: absolute; left: 430px; top: 384px; width: 250px;
    font-family: "Arimo", Arial, sans-serif;
    font-weight: 700; font-size: 66px; line-height: 70px;
    letter-spacing: 26px; color: var(--accent-blue); text-align: center;
    padding-left: 26px;
  }
  .brand-mark {
    position: absolute; left: 496px; top: 556px; width: 240px;
    text-align: center;
  }
  .brand-mark__dot {
    width: 56px; height: 56px; margin: 0 auto 10px;
    border: 3px solid var(--mark-gray); border-radius: 50%;
  }
  .brand-mark__name {
    font-family: "Arimo", Arial, sans-serif;
    font-weight: 400; font-size: 34px; line-height: 40px;
    color: var(--mark-gray);
  }
</style>
</head>
<body>
  <main class="label">
    <svg class="label__sheen" viewBox="0 0 748 752" aria-hidden="true">
      <path d="M748 240 C560 420 520 600 560 752 L748 752 Z" fill="#ffffff" opacity="0.25"/>
    </svg>

    <div class="ghost-feather" role="img" aria-label="Faint embossed feather illustration"></div>
    <p class="ingredients">Ingredients: Water (Aqua), Sodium Laureth Sulfate, Mentha Piperita (Peppermint) Leaf Water, Sodium Lauroyl Oat Amino Acids, Acrylates Copolymer, Cananga Odorata Flower Oil, Melaleuca Alterni folia (Tea Tree) Leaf Oil, Hamamelis Extract, Fragrance</p>

    <div class="divider divider--left"></div>
    <div class="divider divider--right"></div>

    <div class="feather-art" role="img" aria-label="Light blue floating feather illustration"></div>
    <div class="feather-shadow"></div>

    <h1 class="product-name">Cleanser</h1>
    <p class="product-type">GEL</p>

    <div class="brand-mark">
      <div class="brand-mark__dot"></div>
      <p class="brand-mark__name">Fennow Skin Care</p>
    </div>
  </main>
</body>
</html>
```